Pitch Deck Redesign

We are a company in the ed-tech/gaming business wishing to fine-tune the looks of our pitch deck/company presentation.
Attached is the current template we use. And while we want to keep the headlines, general structure and the flow represented in various graphs, we want a design whizz to fine-tune the looks of it, updating graphics and add a bit more graphics. In the end we basically want to give the template a professional edge while still conveying the design philosophy we're trying to achieve, the philosophy is as follows:
A combination of education and playfulness/digital entertainment (particularly gaming). It should additionally be clean, not cluttered yet with a hint of fun.
We of course want to be able to simply ad our own texts as well as our to logo various elements

```html
<!DOCTYPE html>
<html lang="en">
<head>
<meta charset="utf-8">
<title>Quizora – Pitch Deck</title>
<link rel="stylesheet" href="https://fonts.googleapis.com/css2?family=Montserrat:wght@600;700;800&family=Roboto:wght@400;700&display=swap">
<style>
  :root{
    --blue:#2b6cb8;
    --green:#5ea23a;
    --yellow:#f9b710;
    --orange:#e5682a;
    --pale-green:#d9e8cf;
    --ink:#1d1d1f;
    --body:#4a4a4f;
    --canvas:#a7a8aa;
    --card:#f5f6f8;
  }
  *{box-sizing:border-box;margin:0;padding:0}
  html,body{width:1200px;height:3916px;overflow:hidden}
  body{background:var(--canvas);position:relative;font-family:"Roboto",Arial,sans-serif;color:var(--body)}
  .slide{position:absolute;left:114px;width:981px;height:550px;background:#fff;overflow:hidden;box-shadow:0 2px 6px rgba(0,0,0,.12)}
  .decor{position:absolute;inset:0;width:981px;height:550px;pointer-events:none}
  .stripe{position:absolute;left:0;bottom:0;width:100%;height:6px;display:flex}
  .stripe span{flex:1}
  .stripe .s1{background:var(--blue)}.stripe .s2{background:var(--green)}
  .stripe .s3{background:var(--yellow)}.stripe .s4{background:var(--orange)}
  .wordmark{font-family:"Montserrat",Arial,sans-serif;font-weight:800;color:var(--blue);letter-spacing:2px;line-height:1}
  .slide-title{position:absolute;left:61px;top:36px;font-family:"Montserrat",Arial,sans-serif;font-weight:600;font-size:26px;color:var(--ink);padding-left:22px;line-height:30px}
  .slide-title::before{content:"";position:absolute;left:0;top:2px;width:6px;height:26px;background:var(--blue)}
  .slide .wordmark.corner{position:absolute;left:730px;top:34px;font-size:42px}
  .copy p{font-size:11px;line-height:19px;text-align:justify;margin-bottom:12px;color:var(--body)}
  .col-heading{font-family:"Roboto",Arial,sans-serif;font-weight:700;font-size:19px;color:var(--blue);margin-bottom:16px}
  .photo-frame{position:absolute}
  .photo-frame .backing{position:absolute;left:490px;top:152px;width:254px;height:354px;background:var(--blue)}
  .photo-frame .photo{position:absolute;left:506px;top:106px;width:411px;height:380px;box-shadow:0 8px 18px rgba(0,0,0,.3)}
  .stat-list{position:absolute;left:487px;top:114px;width:430px;list-style:none}
  .stat-list li{position:relative;height:84px;margin-bottom:15px;background:var(--card);border-left:3px solid var(--blue);padding:18px 20px 0 42px;font-size:11px;line-height:17px;color:var(--body)}
  .stat-list li svg{position:absolute;left:20px;top:21px}
  .stat-list li.green{border-color:var(--green)}
  .stat-list li.yellow{border-color:var(--yellow)}
  .stat-list li.orange{border-color:var(--orange)}
  .donut{position:absolute;left:0;top:0}
  .donut-label{font-family:"Montserrat",Arial,sans-serif;font-weight:600;font-size:15px;fill:#fff}
  .donut-center{position:absolute;font-size:38px;transform:translate(-50%,-50%)}
</style>
</head>
<body>

<!-- Cover -->
<section class="slide cover" style="top:114px">
  <div role="img" aria-label="Dotted world map" style="position:absolute;left:84px;top:68px;width:813px;height:350px;background:radial-gradient(ellipse at 50% 50%,#e2e3e6 0%,#eeeff1 55%,rgba(255,255,255,0) 75%)"></div>
  <div class="wordmark" style="position:absolute;left:61px;top:250px;font-size:60px">Quizora</div>
  <div style="position:absolute;left:383px;top:160px;width:2px;height:228px;background:#d5d6d9"></div>
  <p style="position:absolute;left:444px;top:190px;width:390px;font-family:'Montserrat',Arial,sans-serif;font-weight:700;font-size:32px;line-height:43px;color:var(--ink)"><span style="color:var(--yellow)">“</span>Turning the billion dollar gaming industry into an education-encouraging tool<span style="color:var(--yellow)">”</span></p>
  <svg class="decor" viewBox="0 0 981 550">
    <polygon points="836,10 926,62 836,112" fill="none" stroke="var(--pale-green)" stroke-width="6" stroke-linejoin="round"/>
    <circle cx="981" cy="123" r="37" fill="var(--blue)"/>
    <rect x="918" y="213" width="9" height="38" rx="4.5" fill="var(--yellow)"/>
    <rect x="918" y="286" width="9" height="38" rx="4.5" fill="var(--yellow)"/>
    <circle cx="862" cy="281" r="28" fill="none" stroke="var(--blue)" stroke-width="6"/>
    <rect x="927" y="375" width="70" height="80" fill="none" stroke="var(--green)" stroke-width="6"/>
    <circle cx="863" cy="497" r="40" fill="var(--orange)"/>
  </svg>
  <div class="stripe"><span class="s1"></span><span class="s2"></span><span class="s3"></span><span class="s4"></span></div>
</section>

<!-- Mission -->
<section class="slide" style="top:739px">
  <svg class="decor" viewBox="0 0 981 550">
    <circle cx="0" cy="212" r="30" fill="var(--orange)"/>
    <polygon points="-10,450 76,490 -10,530" fill="none" stroke="var(--pale-green)" stroke-width="6" stroke-linejoin="round"/>
    <circle cx="981" cy="110" r="35" fill="var(--blue)"/>
    <polygon points="876,116 966,166 876,216" fill="none" stroke="var(--pale-green)" stroke-width="6" stroke-linejoin="round"/>
    <rect x="948" y="198" width="9" height="38" rx="4.5" fill="var(--yellow)"/>
    <rect x="948" y="270" width="9" height="38" rx="4.5" fill="var(--yellow)"/>
    <circle cx="896" cy="342" r="29" fill="none" stroke="var(--blue)" stroke-width="6"/>
    <rect x="934" y="360" width="66" height="80" fill="none" stroke="var(--green)" stroke-width="6"/>
    <circle cx="903" cy="516" r="40" fill="var(--orange)"/>
  </svg>
  <h2 class="slide-title">Mission Statement And Vision</h2>
  <div class="wordmark corner">Quizora</div>
  <div class="copy" style="position:absolute;left:61px;top:126px;width:364px">
    <h3 class="col-heading">MISSION STATEMENT</h3>
    <p>Lorem ipsum dolor sit amet, consectetur adipiscing elit, sed do eiusmod tempor incididunt ut labore et dolore magna aliqua. Ut enim ad minim veniam, quis nostrud exercitation ullamco laboris nisi ut aliquip ex ea commodo consequat. Duis aute irure dolor in reprehenderit in voluptate velit esse cillum dolore eu fugiat nulla pariatur.</p>
    <p>Sed ut perspiciatis unde omnis iste natus error sit voluptatem accusantium doloremque laudantium, totam rem aperiam, eaque ipsa quae ab illo inventore veritatis et quasi architecto beatae vitae dicta sunt explicabo.</p>
    <p>Nemo enim ipsam voluptatem quia voluptas sit aspernatur aut odit aut fugit, sed quia consequuntur magni dolores eos qui ratione voluptatem sequi nesciunt. Neque porro quisquam est, qui dolorem ipsum quia dolor sit amet, consectetur, adipisci velit, sed quia non numquam eius modi tempora incidunt ut labore et dolore voluptatem.</p>
  </div>
  <div class="copy" style="position:absolute;left:479px;top:126px;width:364px">
    <h3 class="col-heading">Vision STATEMENT</h3>
    <p>Lorem ipsum dolor sit amet, consectetur adipiscing elit, sed do eiusmod tempor incididunt ut labore et dolore magna aliqua. Ut enim ad minim veniam, quis nostrud exercitation ullamco laboris nisi ut aliquip ex ea commodo consequat. Duis aute irure dolor in reprehenderit in voluptate velit esse cillum dolore eu fugiat nulla pariatur.</p>
    <p>Sed ut perspiciatis unde omnis iste natus error sit voluptatem accusantium doloremque laudantium, totam rem aperiam, eaque ipsa quae ab illo inventore veritatis et quasi architecto beatae vitae dicta sunt explicabo.</p>
    <p>Nemo enim ipsam voluptatem quia voluptas sit aspernatur aut odit aut fugit, sed quia consequuntur magni dolores eos qui ratione voluptatem sequi nesciunt. Neque porro quisquam est, qui dolorem ipsum quia dolor sit amet, consectetur, adipisci velit, sed quia non numquam eius modi tempora incidunt ut labore et dolore voluptatem.</p>
  </div>
  <div class="stripe"><span class="s1"></span><span class="s2"></span><span class="s3"></span><span class="s4"></span></div>
</section>

<!-- Story -->
<section class="slide" style="top:1365px">
  <svg class="decor" viewBox="0 0 981 550">
    <circle cx="0" cy="212" r="30" fill="var(--orange)"/>
    <polygon points="-10,450 76,490 -10,530" fill="none" stroke="var(--pale-green)" stroke-width="6" stroke-linejoin="round"/>
    <circle cx="981" cy="110" r="35" fill="var(--blue)"/>
    <polygon points="876,116 966,166 876,216" fill="none" stroke="var(--pale-green)" stroke-width="6" stroke-linejoin="round"/>
    <rect x="948" y="198" width="9" height="38" rx="4.5" fill="var(--yellow)"/>
    <rect x="948" y="270" width="9" height="38" rx="4.5" fill="var(--yellow)"/>
    <circle cx="896" cy="342" r="29" fill="none" stroke="var(--blue)" stroke-width="6"/>
    <rect x="934" y="360" width="66" height="80" fill="none" stroke="var(--green)" stroke-width="6"/>
    <circle cx="903" cy="516" r="40" fill="var(--orange)"/>
  </svg>
  <h2 class="slide-title">Story</h2>
  <div class="wordmark corner">Quizora</div>
  <div class="copy" style="position:absolute;left:61px;top:144px;width:364px">
    <p>Lorem ipsum dolor sit amet, consectetur adipiscing elit, sed do eiusmod tempor incididunt ut labore et dolore magna aliqua. Ut enim ad minim veniam, quis nostrud exercitation ullamco laboris nisi ut aliquip ex ea commodo consequat. Duis aute irure dolor in reprehenderit in voluptate velit esse cillum dolore eu fugiat nulla pariatur.</p>
    <p>Sed ut perspiciatis unde omnis iste natus error sit voluptatem accusantium doloremque laudantium, totam rem aperiam, eaque ipsa quae ab illo inventore veritatis et quasi architecto beatae vitae dicta sunt explicabo.</p>
    <p>Nemo enim ipsam voluptatem quia voluptas sit aspernatur aut odit aut fugit, sed quia consequuntur magni dolores eos qui ratione voluptatem sequi nesciunt. Neque porro quisquam est, qui dolorem ipsum quia dolor sit amet, consectetur, adipisci velit, sed quia non numquam eius modi tempora incidunt ut labore et dolore voluptatem.</p>
  </div>
  <div class="photo-frame">
    <div class="backing"></div>
    <div class="photo" role="img" aria-label="Photo of a young gamer at a glowing computer setup" style="background:linear-gradient(135deg,#2a2d6b 0%,#4a3a9a 30%,#1a2a4a 60%,#0d1422 100%)"></div>
  </div>
  <div class="stripe"><span class="s1"></span><span class="s2"></span><span class="s3"></span><span class="s4"></span></div>
</section>

<!-- Why We Exist 1 -->
<section class="slide" style="top:1992px;left:105px">
  <svg class="decor" viewBox="0 0 981 550">
    <circle cx="0" cy="212" r="30" fill="var(--orange)"/>
    <polygon points="-10,450 76,490 -10,530" fill="none" stroke="var(--pale-green)" stroke-width="6" stroke-linejoin="round"/>
    <circle cx="981" cy="110" r="35" fill="var(--blue)"/>
    <polygon points="876,116 966,166 876,216" fill="none" stroke="var(--pale-green)" stroke-width="6" stroke-linejoin="round"/>
    <rect x="948" y="198" width="9" height="38" rx="4.5" fill="var(--yellow)"/>
    <rect x="948" y="270" width="9" height="38" rx="4.5" fill="var(--yellow)"/>
    <circle cx="896" cy="342" r="29" fill="none" stroke="var(--blue)" stroke-width="6"/>
    <rect x="934" y="360" width="66" height="80" fill="none" stroke="var(--green)" stroke-width="6"/>
    <circle cx="903" cy="516" r="40" fill="var(--orange)"/>
  </svg>
  <h2 class="slide-title">Why We Exist</h2>
  <div class="wordmark corner">Quizora</div>
  <svg class="donut" width="981" height="550" viewBox="0 0 981 550">
    <g transform="translate(238,300)" fill="none" stroke-width="72">
      <path d="M4.96,-141.9 A142,142 0 0 1 141.9,-4.96" stroke="var(--green)"/>
      <path d="M141.5,12.4 A142,142 0 0 1 -60,128.7" stroke="var(--yellow)"/>
      <path d="M-75.3,120.4 A142,142 0 0 1 -4.96,-141.9" stroke="var(--blue)"/>
      <path id="lbl-blue" d="M-117.8,68 A136,136 0 0 1 -104.2,-87.4" stroke="none"/>
      <path id="lbl-green" d="M18.9,-134.7 A136,136 0 0 1 135.5,-11.9" stroke="none"/>
      <path id="lbl-yellow" d="M-50.6,139.1 A148,148 0 0 0 145.8,25.7" stroke="none"/>
      <text class="donut-label"><textPath href="#lbl-blue" startOffset="50%" text-anchor="middle">2,8 billion</textPath></text>
      <text class="donut-label"><textPath href="#lbl-green" startOffset="50%" text-anchor="middle">90% Stat description</textPath></text>
      <text class="donut-label"><textPath href="#lbl-yellow" startOffset="50%" text-anchor="middle">9 of10 Stat description</textPath></text>
    </g>
  </svg>
  <div class="wordmark donut-center" style="left:238px;top:300px">Quizora</div>
  <ul class="stat-list">
    <li><svg width="12" height="12" viewBox="0 0 12 12"><circle cx="6" cy="6" r="6" fill="var(--blue)"/><path d="M3.2,6.2 5.2,8 8.8,4.2" fill="none" stroke="#fff" stroke-width="1.6"/></svg>Lorem ipsum dolor sit amet, consectetur adipiscing elit, sed do eiusmod tempor incididunt ut labore et dolore magna aliqua. Ut enim ad minim veniam, ex ea commodo consequat.</li>
    <li class="green"><svg width="12" height="12" viewBox="0 0 12 12"><circle cx="6" cy="6" r="6" fill="var(--green)"/><path d="M3.2,6.2 5.2,8 8.8,4.2" fill="none" stroke="#fff" stroke-width="1.6"/></svg>Lorem ipsum dolor sit amet, consectetur adipiscing elit, sed do eiusmod tempor incididunt ut labore et dolore magna aliqua. Ut enim ad minim veniam, ex ea commodo consequat.</li>
    <li class="yellow"><svg width="12" height="12" viewBox="0 0 12 12"><circle cx="6" cy="6" r="6" fill="var(--yellow)"/><path d="M3.2,6.2 5.2,8 8.8,4.2" fill="none" stroke="#fff" stroke-width="1.6"/></svg>Lorem ipsum dolor sit amet, consectetur adipiscing elit, sed do eiusmod tempor incididunt ut labore et dolore magna aliqua. Ut enim ad minim veniam, ex ea commodo consequat.</li>
    <li class="orange"><svg width="12" height="12" viewBox="0 0 12 12"><circle cx="6" cy="6" r="6" fill="var(--orange)"/><path d="M3.2,6.2 5.2,8 8.8,4.2" fill="none" stroke="#fff" stroke-width="1.6"/></svg>Lorem ipsum dolor sit amet, consectetur adipiscing elit, sed do eiusmod tempor incididunt ut labore et dolore magna aliqua. Ut enim ad minim veniam, ex ea commodo consequat.</li>
  </ul>
  <div class="stripe"><span class="s1"></span><span class="s2"></span><span class="s3"></span><span class="s4"></span></div>
</section>

<!-- Why We Exist 2 -->
<section class="slide" style="top:2619px">
  <svg class="decor" viewBox="0 0 981 550">
    <circle cx="0" cy="212" r="30" fill="var(--orange)"/>
    <polygon points="-10,450 76,490 -10,530" fill="none" stroke="var(--pale-green)" stroke-width="6" stroke-linejoin="round"/>
    <circle cx="981" cy="110" r="35" fill="var(--blue)"/>
    <polygon points="876,116 966,166 876,216" fill="none" stroke="var(--pale-green)" stroke-width="6" stroke-linejoin="round"/>
    <rect x="948" y="198" width="9" height="38" rx="4.5" fill="var(--yellow)"/>
    <rect x="948" y="270" width="9" height="38" rx="4.5" fill="var(--yellow)"/>
    <circle cx="896" cy="342" r="29" fill="none" stroke="var(--blue)" stroke-width="6"/>
    <rect x="934" y="360" width="66" height="80" fill="none" stroke="var(--green)" stroke-width="6"/>
    <circle cx="903" cy="516" r="40" fill="var(--orange)"/>
  </svg>
  <h2 class="slide-title">Why We Exist</h2>
  <div class="wordmark corner">Quizora</div>
  <svg class="donut" width="981" height="550" viewBox="0 0 981 550">
    <g transform="translate(237,304)" fill="none" stroke-width="92">
      <path d="M4.7,-134.9 A135,135 0 0 1 134.9,-4.7" stroke="var(--green)"/>
      <path d="M134.5,11.8 A135,135 0 0 1 -90.3,100.3" stroke="var(--blue)"/>
      <path d="M-100.3,90.3 A135,135 0 0 1 -116.9,-67.5" stroke="var(--yellow)"/>
      <path d="M-107.8,-81.3 A135,135 0 0 1 -11.8,-134.5" stroke="var(--orange)"/>
      <g class="donut-label" text-anchor="middle" dominant-baseline="middle">
        <text x="95" y="-95">30%</text>
        <text x="50.6" y="125">43%</text>
        <text x="-134" y="14">1of 5</text>
        <text x="-65.5" y="-118">15,7%</text>
      </g>
    </g>
  </svg>
  <div class="wordmark donut-center" style="left:237px;top:304px">Quizora</div>
  <ul class="stat-list">
    <li><svg width="12" height="12" viewBox="0 0 12 12"><circle cx="6" cy="6" r="6" fill="var(--blue)"/><path d="M3.2,6.2 5.2,8 8.8,4.2" fill="none" stroke="#fff" stroke-width="1.6"/></svg>Lorem ipsum dolor sit amet, consectetur adipiscing elit, sed do eiusmod tempor incididunt ut labore et dolore magna aliqua. Ut enim ad minim veniam, ex ea commodo consequat.</li>
    <li class="green"><svg width="12" height="12" viewBox="0 0 12 12"><circle cx="6" cy="6" r="6" fill="var(--green)"/><path d="M3.2,6.2 5.2,8 8.8,4.2" fill="none" stroke="#fff" stroke-width="1.6"/></svg>Lorem ipsum dolor sit amet, consectetur adipiscing elit, sed do eiusmod tempor incididunt ut labore et dolore magna aliqua. Ut enim ad minim veniam, ex ea commodo consequat.</li>
    <li class="yellow"><svg width="12" height="12" viewBox="0 0 12 12"><circle cx="6" cy="6" r="6" fill="var(--yellow)"/><path d="M3.2,6.2 5.2,8 8.8,4.2" fill="none" stroke="#fff" stroke-width="1.6"/></svg>Lorem ipsum dolor sit amet, consectetur adipiscing elit, sed do eiusmod tempor incididunt ut labore et dolore magna aliqua. Ut enim ad minim veniam, ex ea commodo consequat.</li>
    <li class="orange"><svg width="12" height="12" viewBox="0 0 12 12"><circle cx="6" cy="6" r="6" fill="var(--orange)"/><path d="M3.2,6.2 5.2,8 8.8,4.2" fill="none" stroke="#fff" stroke-width="1.6"/></svg>Lorem ipsum dolor sit amet, consectetur adipiscing elit, sed do eiusmod tempor incididunt ut labore et dolore magna aliqua. Ut enim ad minim veniam, ex ea commodo consequat.</li>
  </ul>
  <div class="stripe"><span class="s1"></span><span class="s2"></span><span class="s3"></span><span class="s4"></span></div>
</section>

<!-- Our Solution -->
<section class="slide" style="top:3246px;left:110px">
  <svg class="decor" viewBox="0 0 981 550">
    <circle cx="0" cy="212" r="30" fill="var(--orange)"/>
    <polygon points="-10,450 76,490 -10,530" fill="none" stroke="var(--pale-green)" stroke-width="6" stroke-linejoin="round"/>
    <circle cx="981" cy="110" r="35" fill="var(--blue)"/>
    <polygon points="876,116 966,166 876,216" fill="none" stroke="var(--pale-green)" stroke-width="6" stroke-linejoin="round"/>
    <rect x="948" y="198" width="9" height="38" rx="4.5" fill="var(--yellow)"/>
    <rect x="948" y="270" width="9" height="38" rx="4.5" fill="var(--yellow)"/>
    <circle cx="896" cy="342" r="29" fill="none" stroke="var(--blue)" stroke-width="6"/>
    <rect x="934" y="360" width="66" height="80" fill="none" stroke="var(--green)" stroke-width="6"/>
    <circle cx="903" cy="516" r="40" fill="var(--orange)"/>
  </svg>
  <h2 class="slide-title">Our Solution</h2>
  <div class="wordmark corner">Quizora</div>
  <div class="copy" style="position:absolute;left:61px;top:144px;width:364px">
    <p>Lorem ipsum dolor sit amet, consectetur adipiscing elit, sed do eiusmod tempor incididunt ut labore et dolore magna aliqua. Ut enim ad minim veniam, quis nostrud exercitation ullamco laboris nisi ut aliquip ex ea commodo consequat. Duis aute irure dolor in reprehenderit in voluptate velit esse cillum dolore eu fugiat nulla pariatur.</p>
    <p>Sed ut perspiciatis unde omnis iste natus error sit voluptatem accusantium doloremque laudantium, totam rem aperiam, eaque ipsa quae ab illo inventore veritatis et quasi architecto beatae vitae dicta sunt explicabo.</p>
    <p>Nemo enim ipsam voluptatem quia voluptas sit aspernatur aut odit aut fugit, sed quia consequuntur magni dolores eos qui ratione voluptatem sequi nesciunt. Neque porro quisquam est, qui dolorem ipsum quia dolor sit amet, consectetur, adipisci velit, sed quia non numquam eius modi tempora incidunt ut labore et dolore voluptatem.</p>
  </div>
  <div class="photo-frame">
    <div class="backing"></div>
    <div class="photo" role="img" aria-label="Photo of a parent and two children playing video games together" style="background:linear-gradient(135deg,#d9d6cf 0%,#8a7566 35%,#3d4f6a 65%,#2a2e3a 100%)"></div>
  </div>
  <div class="stripe"><span class="s1"></span><span class="s2"></span><span class="s3"></span><span class="s4"></span></div>
</section>

</body>
</html>
```